Laundromat wall mural with logo, wash steps and soap dish instructions

Hi,
I am building a new laundromat and want to design a large wall mural containing a few different sections. The first piece would be a large image of my logo "Suds Harbor Laundromat" with my new tag line under it "A better Place to Wash". The next section would be general washing instructions: (step1) load clothes, (step 2) load soap, (step 3) select cycle (step 4) present payment (Quarters, Credit Card or Fennix/trove pay) (Step 5) Press start. Please use the wave from the logo to encase each of these 5 steps. Also please use an emblem in each wave to show each sections action. Such as they did in one of the example files I attached to this brief. The Final section would be the design for the soap compartment, describing where it goes. Please place the title "Where does the soap go?" above this section. The whole wall section will be 40 feet wide and 5 feet tall. I would like each section to flow aesthetically into the other. Feel free to use the logos waves and colors to bring everything together. I have attached examples of other store designs that I have found. The design will be above the washers that are placed against the wall.
I also placed a design of the mural that I wasn't completely impressed with so I opened the project to more designers.

Please let me know what other info you need.

Bests

Target Market(s)

laundromat customers

Industry/Entity Type

Laundromat

Font styles to use
Sans Serif

Colors
0054AA
0677BA
7BADD7
CADEEF
E8F1F8

Requirements
Must have
• The wave from my logo continuously flowing around the side and bottom borders.

```html
<!DOCTYPE html>
<html lang="en">
<head>
<meta charset="utf-8">
<title>Suds Harbor Laundromat – Wall Mural</title>
<link href="https://fonts.googleapis.com/css2?family=Montserrat:ital,wght@0,600;0,700;1,800;1,900&display=swap" rel="stylesheet">
<style>
  :root {
    --navy: #0054AA;
    --blue: #0677BA;
    --sky: #7BADD7;
    --mist: #CADEEF;
    --foam: #E8F1F8;
    --ink: #111111;
    --white: #ffffff;
    --stage: #e6e4e5;
  }
  * { box-sizing: border-box; margin: 0; padding: 0; }
  html, body { width: 1200px; height: 205px; overflow: hidden; background: var(--stage); }
  body { position: relative; font-family: "Montserrat", Arial, sans-serif; }

  .mural {
    position: absolute; left: 36px; top: 32px; width: 1128px; height: 140px;
    background: var(--white); overflow: hidden;
  }
  .mural-waves { position: absolute; left: 0; top: 0; width: 1128px; height: 140px; }

  .brand { position: absolute; left: 22px; top: 14px; }
  .brand-name {
    display: flex; align-items: center; gap: 6px;
    font-weight: 700; font-size: 15px; line-height: 1.05; color: var(--navy);
    text-transform: uppercase;
  }
  .brand-dot { width: 14px; height: 14px; border-radius: 50%; background: var(--blue); flex: none; }
  .tagline {
    margin-top: 12px; font-style: italic; font-weight: 900; text-transform: uppercase;
    font-size: 15px; line-height: 1.1; letter-spacing: .3px;
  }
  .tagline-top { color: var(--ink); display: block; }
  .tagline-bottom { color: var(--blue); display: block; padding-left: 4px; }

  .step { position: absolute; top: 0; width: 120px; height: 140px; }
  .step-number {
    position: absolute; left: 0; top: 22px;
    font-style: italic; font-weight: 900; font-size: 30px; color: var(--ink);
  }
  .step-disc { position: absolute; left: 12px; top: 12px; width: 98px; height: 98px; }
  .step-label {
    position: absolute; left: 26px; top: 44px; width: 70px;
    text-align: center; color: var(--white); font-weight: 600; font-size: 11.5px; line-height: 1.25;
  }
  .step-icon {
    position: absolute; left: 24px; top: 84px; width: 34px; height: 34px; border-radius: 50%;
    background: var(--white); box-shadow: 0 1px 3px rgba(0,0,0,.25);
    display: flex; align-items: center; justify-content: center;
  }
  .step-icon-art { width: 22px; height: 22px; border-radius: 50%; background: linear-gradient(135deg, var(--sky), var(--mist)); }

  .soap-title {
    position: absolute; left: 848px; top: 40px;
    font-style: italic; font-weight: 900; text-transform: uppercase; font-size: 17px; line-height: 1.05;
  }
  .soap-title-top { display: block; color: var(--ink); }
  .soap-title-bottom { display: block; color: var(--blue); }

  .soap-dispenser {
    position: absolute; left: 996px; top: 12px; width: 120px; height: 116px;
    border-radius: 6px; background: linear-gradient(160deg, #8a8c90, #5a5c60 55%, var(--sky));
  }
</style>
</head>
<body>
<main class="mural">
  <svg class="mural-waves" viewBox="0 0 1128 140" aria-hidden="true">
    <path d="M0 118 C120 102 240 130 380 120 C520 110 560 136 700 124 C830 112 900 124 1000 112 C1060 106 1100 108 1128 104 L1128 140 L0 140 Z" fill="var(--blue)"/>
    <path d="M0 124 C140 110 260 134 400 126 C540 118 580 140 720 130 C850 120 920 130 1010 118 C1070 112 1110 114 1128 112" fill="none" stroke="var(--white)" stroke-width="2"/>
    <path d="M0 112 C80 98 200 124 320 116" fill="none" stroke="var(--sky)" stroke-width="1.5" opacity=".7"/>
  </svg>

  <header class="brand">
    <div class="brand-name"><span class="brand-dot"></span><span>Suds Harbor<br>Laundromat</span></div>
    <p class="tagline"><span class="tagline-top">A Better Place</span><span class="tagline-bottom">To Wash</span></p>
  </header>

  <section class="steps">
    <div class="step" style="left:228px">
      <span class="step-number">1</span>
      <svg class="step-disc" viewBox="0 0 98 98" aria-hidden="true"><defs><radialGradient id="g" cx="50%" cy="40%" r="60%"><stop offset="0" stop-color="#5fa3d6"/><stop offset="1" stop-color="var(--blue)"/></radialGradient></defs><circle cx="49" cy="49" r="47" fill="none" stroke="var(--blue)" stroke-width="2.5"/><circle cx="49" cy="49" r="42" fill="url(#g)"/></svg>
      <p class="step-label">Load Clothes</p>
      <div class="step-icon"><div class="step-icon-art" role="img" aria-label="Washing machine icon"></div></div>
    </div>
    <div class="step" style="left:352px">
      <span class="step-number">2</span>
      <svg class="step-disc" viewBox="0 0 98 98" aria-hidden="true"><circle cx="49" cy="49" r="47" fill="none" stroke="var(--blue)" stroke-width="2.5"/><circle cx="49" cy="49" r="42" fill="url(#g)"/></svg>
      <p class="step-label">Load Soap</p>
      <div class="step-icon"><div class="step-icon-art" role="img" aria-label="Detergent bottle icon"></div></div>
    </div>
    <div class="step" style="left:476px">
      <span class="step-number">3</span>
      <svg class="step-disc" viewBox="0 0 98 98" aria-hidden="true"><circle cx="49" cy="49" r="47" fill="none" stroke="var(--blue)" stroke-width="2.5"/><circle cx="49" cy="49" r="42" fill="url(#g)"/></svg>
      <p class="step-label">Select Cycle</p>
      <div class="step-icon">
        <svg width="22" height="22" viewBox="0 0 22 22" aria-label="Power button icon" role="img"><circle cx="11" cy="11" r="10" fill="var(--foam)" stroke="var(--sky)"/><path d="M7.5 8 A5 5 0 1 0 14.5 8" fill="none" stroke="var(--blue)" stroke-width="1.6" stroke-linecap="round"/><line x1="11" y1="5.5" x2="11" y2="11" stroke="var(--blue)" stroke-width="1.6" stroke-linecap="round"/></svg>
      </div>
    </div>
    <div class="step" style="left:600px">
      <span class="step-number">4</span>
      <svg class="step-disc" viewBox="0 0 98 98" aria-hidden="true"><circle cx="49" cy="49" r="47" fill="none" stroke="var(--blue)" stroke-width="2.5"/><circle cx="49" cy="49" r="42" fill="url(#g)"/></svg>
      <p class="step-label">Present Payment</p>
      <div class="step-icon"><div class="step-icon-art" role="img" aria-label="Hand holding coin icon"></div></div>
    </div>
    <div class="step" style="left:724px">
      <span class="step-number">5</span>
      <svg class="step-disc" viewBox="0 0 98 98" aria-hidden="true"><circle cx="49" cy="49" r="47" fill="none" stroke="var(--blue)" stroke-width="2.5"/><circle cx="49" cy="49" r="42" fill="url(#g)"/></svg>
      <p class="step-label">Press Start</p>
      <div class="step-icon"><div class="step-icon-art" role="img" aria-label="Finger pressing button icon"></div></div>
    </div>
  </section>

  <h2 class="soap-title"><span class="soap-title-top">Where</span><span class="soap-title-bottom">Does the<br>Soap Go!</span></h2>
  <div class="soap-dispenser" role="img" aria-label="Washer soap compartment diagram showing fabric softener, liquid detergent or bleach, and detergent slots"></div>
</main>
</body>
</html>
```